RB Business Card Design

My company provides advising/training and coaching services to business owners who want better financial results and better work/life balance. We help them through creating custom plans supported with education, strategic thinking and accountability.

We also help through some online courses which are geared to smaller businesses.
Updates

please also include our nth american contact # +1 555 382 6071

Industry/Entity Type

Financial

Contact Information for Business Card

Perry Valdane
perry@perryvaldane.net
+61 455 713 902
www.perryvaldane.net

```html
<!DOCTYPE html>
<html lang="en">
<head>
<meta charset="utf-8">
<title>Perry Valdane Business Card</title>
<link rel="stylesheet" href="https://fonts.googleapis.com/css2?family=Arimo:wght@400&display=swap">
<style>
  :root {
    --backdrop: #d9d2c7;
    --card: #000000;
    --accent-blue: #1b7fd1;
    --logo-grey: #a7a7a7;
    --formula-grey: #b5b5b5;
  }
  html, body {
    margin: 0;
    padding: 0;
    width: 1200px;
    height: 870px;
    overflow: hidden;
    background: var(--backdrop);
    font-family: "Arimo", Arial, sans-serif;
  }
  .sheet {
    position: relative;
    width: 1200px;
    height: 870px;
    display: flex;
    justify-content: center;
    align-items: center;
    gap: 80px;
  }
  .card {
    width: 340px;
    height: 595px;
    background: var(--card);
    box-shadow: 0 6px 18px rgba(0,0,0,0.25);
    display: flex;
    flex-direction: column;
    align-items: center;
    box-sizing: border-box;
  }
  .brand {
    display: flex;
    flex-direction: column;
    align-items: center;
    gap: 18px;
  }
  .brand-dot {
    width: 46px;
    height: 46px;
    border-radius: 50%;
    background: var(--accent-blue);
  }
  .brand-name {
    color: var(--logo-grey);
    font-size: 25px;
    font-weight: 400;
    letter-spacing: 0.5px;
    text-transform: uppercase;
    margin: 0;
  }
  .card-front { padding-top: 120px; }
  .contact-list {
    list-style: none;
    margin: 95px 0 0;
    padding: 0;
    text-align: center;
    color: var(--accent-blue);
    font-size: 21px;
    line-height: 44px;
  }
  .card-back { padding-top: 120px; }
  .formula {
    margin-top: 80px;
    display: flex;
    flex-direction: column;
    align-items: center;
    gap: 8px;
    font-size: 21px;
  }
  .formula-term { color: var(--accent-blue); }
  .formula-operator {
    color: var(--formula-grey);
    font-size: 26px;
    line-height: 26px;
  }
</style>
</head>
<body>
<main class="sheet">
  <section class="card card-front" aria-label="Card front">
    <div class="brand">
      <span class="brand-dot"></span>
      <h1 class="brand-name">Perry Valdane</h1>
    </div>
    <ul class="contact-list">
      <li>+1 555 382 6071</li>
      <li>+61 455 713 902</li>
      <li>perry@perryvaldane.net</li>
      <li>www.perryvaldane.net</li>
    </ul>
  </section>

  <section class="card card-back" aria-label="Card back">
    <div class="brand">
      <span class="brand-dot"></span>
      <p class="brand-name">Perry Valdane</p>
    </div>
    <div class="formula">
      <span class="formula-term">Knowledge</span>
      <span class="formula-operator">+</span>
      <span class="formula-term">Planning</span>
      <span class="formula-operator">*</span>
      <span class="formula-term">Action</span>
      <span class="formula-operator">=</span>
      <span class="formula-term">Success</span>
    </div>
  </section>
</main>
</body>
</html>
```